Create business cards for TallowBay.com.au

TallowBay is a property maintenance group. They mainly do lawns and gardens.
We have a logo designed which can be found attached. We would like to have the design based on the logos theme and look. Pick whatever logo from the files to incorporate in your design as there are a few alterations

Looking for a 2 sided business card that shows a professional yet personal business approach to property maintenance
We want to keep colours bright and we want something unique that drives a call, message, visit the webpage and/or book in

We will need a broshure made after this contest as well.

Some information you may choose to be involved -

Tallow Bay Property Group
Professional yet Personal
visit - [url removed, login to view]
Message or Call- 0487625140
email - xxxxx@[url removed, login to view] (name not selected yet eg bookings@, info@, mowmylawn@, myhouse@[url removed, login to view] )

```html
<!DOCTYPE html>
<html lang="en">
<head>
<meta charset="utf-8">
<title>TallowBay Business Card</title>
<link rel="stylesheet" href="https://fonts.googleapis.com/css2?family=PT+Sans:wght@400;700&family=Ubuntu:wght@500;700&display=swap">
<style>
  :root {
    --page: #ebe8e3;
    --card-white: #ffffff;
    --grass-light: #7fd13a;
    --grass-mid: #4fae22;
    --grass-dark: #2f8a14;
    --brand-green: #8bbf2c;
    --brand-orange: #f2951e;
    --brand-blue: #2a9bd6;
    --ink-grey: #6f6f6f;
    --name-green: #4f8f2a;
  }
  * { margin: 0; padding: 0; box-sizing: border-box; }
  html, body {
    width: 749px;
    height: 1200px;
    overflow: hidden;
    background: var(--page);
  }
  .sheet {
    position: relative;
    width: 749px;
    height: 1200px;
  }
  .card {
    position: absolute;
    left: 64px;
    width: 620px;
    height: 354px;
    overflow: hidden;
    box-shadow: 0 6px 18px rgba(0,0,0,0.18);
  }

  /* Front side */
  .card-front { top: 150px; }
  .grass-field {
    position: absolute;
    inset: 0;
    background:
      radial-gradient(circle at 35% 45%, var(--grass-light) 0%, transparent 55%),
      linear-gradient(135deg, var(--grass-mid) 0%, var(--grass-dark) 100%);
  }
  .front-name {
    position: absolute;
    right: 34px;
    bottom: 40px;
    font-family: "Ubuntu", sans-serif;
    font-weight: 700;
    font-size: 34px;
    color: #ffffff;
    letter-spacing: 0.3px;
  }

  /* Back side */
  .card-back {
    top: 700px;
    background: var(--card-white);
  }
  .back-brand {
    position: absolute;
    left: 30px;
    top: 40px;
    width: 90px;
    height: 290px;
  }
  .back-brand .wordmark {
    position: absolute;
    left: 50%;
    top: 118px;
    transform: translate(-50%, -50%) rotate(-90deg);
    font-family: "Ubuntu", sans-serif;
    font-weight: 700;
    font-size: 30px;
    color: var(--name-green);
    white-space: nowrap;
  }
  .back-brand .dot {
    position: absolute;
    left: 50%;
    bottom: 14px;
    width: 40px;
    height: 40px;
    margin-left: -20px;
    border-radius: 50%;
    background: var(--brand-green);
  }
  .rule-set {
    position: absolute;
    left: 150px;
    top: 0;
    width: 40px;
    height: 320px;
  }
  .contact {
    position: absolute;
    left: 210px;
    top: 92px;
    font-family: "PT Sans", sans-serif;
  }
  .contact .company {
    font-size: 13px;
    letter-spacing: 2.2px;
    color: var(--brand-green);
  }
  .contact .company .accent { color: var(--brand-orange); }
  .contact .tagline {
    margin-top: 2px;
    font-size: 13px;
    letter-spacing: 2.2px;
    color: var(--ink-grey);
  }
  .contact .line {
    font-size: 21px;
    line-height: 1;
  }
  .contact .phone { margin-top: 90px; color: var(--brand-green); }
  .contact .web { margin-top: 22px; color: var(--brand-orange); }
  .contact .mail { margin-top: 22px; color: var(--brand-blue); }
</style>
</head>
<body>
<main class="sheet">

  <section class="card card-front" aria-label="Card front">
    <div class="grass-field" role="img" aria-label="Close-up photograph of a green lawn"></div>
    <p class="front-name">TallowBay.com.au</p>
  </section>

  <section class="card card-back" aria-label="Card back">
    <div class="back-brand">
      <span class="wordmark">TallowBay</span>
      <span class="dot"></span>
    </div>

    <svg class="rule-set" viewBox="0 0 40 320" aria-hidden="true">
      <line x1="6" y1="0" x2="6" y2="320" stroke="var(--brand-blue)" stroke-width="4"/>
      <line x1="18" y1="0" x2="18" y2="290" stroke="var(--brand-orange)" stroke-width="4"/>
      <line x1="30" y1="0" x2="30" y2="260" stroke="var(--brand-green)" stroke-width="4"/>
    </svg>

    <div class="contact">
      <p class="company">Tallow Bay <span class="accent">Property Group</span></p>
      <p class="tagline">Professional yet Personal</p>
      <p class="line phone">0487625140</p>
      <p class="line web">TallowBay.com.au</p>
      <p class="line mail">xxxxx@TallowBay.com.au</p>
    </div>
  </section>

</main>
</body>
</html>
```